A4 Brochure Creation - Exciting Product

I want something designed for a new breakthrough product
I have attached an example of another product design done Infrared Thermomoter
But I want this one looking much much more professional than that example

I want it to be a quick easy to understand brochure powerful on the ability to report by cloud

Target Market(s)

Pubs Clubs Business AgedCare anyone with people entering

Industry/Entity Type

Security Device

Colors
00a990
0792cd

Requirements
Must have
• Applicable to Entrances in Aged Care, hotels, office buildings, schools, shopping malls, shops, communities, public services and management projects that need to use face access to control access and health keeping.

Secure Door Control by easily interfacing to the output relay ensuring only visitors or staff with body temperatures within normal range to gain access.

Payroll Sign In Systems which include existing fingerprint scanning technologies can easily be interfaced ensuring all staff member are within safe temperature ranges before commencing their shits.

Blacklisting is available by our cloud application ensuring someone whom does not have any authority to ever enter a building will not gain access when interfaced to the access control system.
Nice to have
• Executives and Decision makers to be wowed
Should not have
• No flow

```html
<!DOCTYPE html>
<html lang="en">
<head>
<meta charset="utf-8">
<title>Vantora Health – Facial Recognition with Thermal Imaging Brochure</title>
<link href="https://fonts.googleapis.com/css2?family=Montserrat:wght@400;600;700;800&family=Open+Sans:wght@400;600&display=swap" rel="stylesheet">
<style>
:root{
  --teal:#00a990;
  --blue:#0792cd;
  --navy:#17508f;
  --red:#d9262c;
  --ink:#33393f;
  --muted:#6c7379;
  --paper:#ffffff;
  --page-bg:#ffffff;
  --photo-a:#c9d3db;
  --photo-b:#9fb0bd;
  --line:#d8dee3;
}
*{box-sizing:border-box;margin:0;padding:0}
html,body{width:668px;height:1200px;overflow:hidden;background:var(--page-bg)}
body{position:relative;font-family:"Open Sans",Arial,sans-serif;color:var(--ink)}
.spread{position:absolute;left:30px;width:608px;display:flex;box-shadow:0 3px 10px rgba(0,0,0,.25);background:var(--paper)}
.page{position:relative;width:304px;height:100%;overflow:hidden;background:var(--paper)}
.page+.page{border-left:1px solid #e5e9ec}
.photo{position:absolute;background:linear-gradient(135deg,var(--photo-a),var(--photo-b))}
.brand{position:absolute;font-family:"Montserrat",Arial,sans-serif;font-weight:800;font-size:13px;line-height:1.2;color:var(--navy);display:flex;align-items:center;gap:4px;letter-spacing:.2px}
.brand i{display:block;width:9px;height:9px;border-radius:50%;background:var(--teal)}
.brand.light{color:#fff}
.h{font-family:"Montserrat",Arial,sans-serif;font-weight:800;text-transform:uppercase;line-height:1.2}
.copy{position:absolute;font-size:5.2px;line-height:1.45;color:var(--muted)}
.badge{position:absolute;border-radius:50%;background:var(--red);color:#fff;font-family:"Montserrat",Arial,sans-serif;font-weight:800;font-size:5.5px;text-align:center;display:flex;align-items:center;justify-content:center;line-height:1.15;border:2px solid #fff;box-shadow:0 1px 3px rgba(0,0,0,.3)}
.svgfill{position:absolute;left:0;top:0}
.box-text{position:absolute;padding:5px;font-size:5px;line-height:1.45;color:#fff}
ul.list{list-style:none;font-size:5.2px;line-height:1.6;color:#fff}
ul.list li::before{content:"✓ ";color:#fff;font-weight:700}
.spec-title{position:absolute;left:14px;top:14px;width:276px;height:18px;background:var(--blue);padding:0 6px;display:flex;align-items:center;font-size:7px;color:#fff}
.spec{position:absolute;border-collapse:collapse;font-size:4.6px;line-height:1.2;color:var(--ink)}
.spec td{border:1px solid var(--line);padding:1.6px 3px;height:10.4px}
.spec td.k{background:#eef4f8;font-weight:600;width:62px}
.spec td.g{background:var(--blue);color:#fff;font-weight:600;width:34px;text-align:center}
</style>
</head>
<body>

<!-- Spread 1: back and front cover -->
<section class="spread cover" style="top:12px;height:420px">
  <div class="page back-cover">
    <div class="brand" style="left:18px;top:18px"><i></i>Vantora Health</div>
    <div class="h" style="position:absolute;left:18px;top:44px;width:272px;font-size:8.5px;color:var(--blue)">Suitable for aged care, hospitals, hotels,<br>offices, schools, workplaces</div>
    <p class="copy" style="left:18px;top:70px;width:270px">Since 2020 we have supported venues across the country with smart entry screening. Our thermal facial recognition unit checks every visitor in under a second, logs each result to the cloud and gives managers instant reports from any device, so every entrance stays safe and simple.</p>
    <div class="photo" role="img" aria-label="Collage of photos showing the device in use at reception desks and entrances" style="left:18px;top:118px;width:185px;height:122px"></div>
    <div class="photo" role="img" aria-label="Photo of staff passing a screening terminal" style="left:208px;top:118px;width:78px;height:60px"></div>
    <div class="photo" role="img" aria-label="Photo of a visitor at a building entrance" style="left:208px;top:182px;width:78px;height:58px"></div>
    <svg class="svgfill" width="304" height="420" viewBox="0 0 304 420" aria-hidden="true">
      <polygon points="0,268 304,300 304,420 0,420" fill="var(--blue)"/>
      <polygon points="190,330 304,300 304,420 230,420" fill="var(--teal)"/>
    </svg>
    <div class="badge" style="left:222px;top:232px;width:54px;height:54px">ON-SPOT<br>BODY<br>TEMPERATURE</div>
    <div class="h" style="position:absolute;left:18px;top:300px;font-size:10px;color:#fff;text-transform:none">Contact Us</div>
    <div style="position:absolute;left:18px;top:320px;font-size:5.6px;line-height:2.1;color:#fff">
      <div>☎ 1300 555 018</div>
      <div>☎ 02 5550 4172</div>
      <div>✉ hello@vantorahealth.com.au</div>
      <div>⌂ 12 Harbour Row, Fairview NSW 2000</div>
    </div>
  </div>

  <div class="page front-cover">
    <div class="brand" style="left:0;width:304px;justify-content:center;top:18px">Vantora Health</div>
    <svg class="svgfill" width="304" height="420" viewBox="0 0 304 420" aria-hidden="true">
      <path d="M0,58 H304 V100 H0 Z" fill="var(--blue)"/>
      <path d="M0,100 H304 V106 Q150,118 0,106 Z" fill="var(--teal)"/>
      <polygon points="0,360 304,330 304,420 0,420" fill="var(--teal)"/>
      <polygon points="0,372 304,344 304,420 0,420" fill="var(--blue)" opacity=".55"/>
    </svg>
    <div class="h" style="position:absolute;left:0;top:64px;width:304px;text-align:center;font-size:11.5px;color:#fff">Facial recognition with<br><span style="font-size:15px">thermal imaging</span></div>
    <div class="photo" role="img" aria-label="Product photo of the facial recognition thermal terminal on a stand" style="left:72px;top:122px;width:150px;height:170px;border-radius:4px"></div>
    <div class="badge" style="left:236px;top:150px;width:54px;height:54px">ON-SPOT<br>BODY<br>TEMPERATURE</div>
    <p class="copy" style="left:60px;top:298px;width:90px;font-size:4.8px">Screen every entry. Log every result. Report from the cloud.</p>
    <p class="copy" style="left:178px;top:298px;width:110px;font-size:5px;color:var(--navy);font-weight:600;text-transform:uppercase">Fast contact-free screening with live cloud reports</p>
    <div class="h" style="position:absolute;left:0;top:392px;width:304px;text-align:center;font-size:8px;color:#fff;text-transform:none">www.vantorahealth.com.au</div>
  </div>
</section>

<!-- Spread 2: inside pages -->
<section class="spread inside" style="top:444px;height:316px">
  <div class="page intro">
    <svg class="svgfill" width="304" height="316" viewBox="0 0 304 316" aria-hidden="true">
      <rect width="304" height="62" fill="var(--blue)"/>
      <polygon points="0,62 304,62 304,66 0,72" fill="var(--teal)"/>
      <polygon points="0,258 304,246 304,316 0,316" fill="var(--teal)"/>
    </svg>
    <div class="brand light" style="left:16px;top:10px">Vantora Health</div>
    <div class="h" style="position:absolute;left:16px;top:30px;width:200px;font-size:6.5px;color:#fff">AI thermal imaging face temperature<br>measuring intelligent terminals</div>
    <div class="photo" role="img" aria-label="Photo of the terminal screen showing a temperature reading" style="left:226px;top:10px;width:62px;height:70px"></div>
    <div class="h" style="position:absolute;left:16px;top:86px;font-size:7px;color:var(--navy)">Product description</div>
    <p class="copy" style="left:16px;top:98px;width:272px">The terminal combines face recognition and thermal imaging to check visitors at the door in one step. It reads temperature without contact, matches faces against the staff list and sends every record to the cloud portal. Managers view daily reports, export sign-in lists and set alerts for any reading outside the normal range.</p>
    <div class="photo" role="img" aria-label="Photos of the terminal mounted at a turnstile and on a desk" style="left:16px;top:146px;width:272px;height:58px"></div>
    <div style="position:absolute;left:16px;top:212px;width:272px;height:70px;background:var(--blue);padding:6px">
      <div class="h" style="font-size:6.5px;color:#fff">Application scenarios</div>
      <p style="font-size:5px;line-height:1.45;color:#fff;width:120px;margin-top:3px">Aged care, hotels, offices, schools, malls, shops, clubs and any site with people entering.</p>
      <div class="photo" role="img" aria-label="Grid of photos of venues where the terminal is used" style="left:138px;top:6px;width:128px;height:58px"></div>
    </div>
  </div>
  <div class="page uses">
    <div class="box-text" style="left:14px;top:12px;width:108px;height:52px;background:var(--blue)">Blacklisting is available through our cloud app so anyone without authority is never granted entry.</div>
    <div class="photo" role="img" aria-label="Photo of the cloud reporting dashboard on a tablet" style="left:130px;top:12px;width:160px;height:52px"></div>
    <div class="photo" role="img" aria-label="Photo of an aged care entrance" style="left:14px;top:72px;width:126px;height:64px"></div>
    <div class="box-text" style="left:148px;top:72px;width:142px;height:64px;background:var(--teal)">Applicable to entrances in aged care, hotels, office buildings, schools, shopping malls, shops and public services that need face access and health checks.</div>
    <div class="box-text" style="left:14px;top:144px;width:126px;height:64px;background:var(--blue)">Secure door control by linking to the output relay, so only people within the normal range gain access.</div>
    <div class="photo" role="img" aria-label="Photo of a door access controller" style="left:148px;top:144px;width:142px;height:64px"></div>
    <div class="photo" role="img" aria-label="Photo of staff using a payroll sign-in scanner" style="left:14px;top:216px;width:126px;height:64px"></div>
    <div class="box-text" style="left:148px;top:216px;width:142px;height:64px;background:var(--teal)">Payroll sign-in systems, including fingerprint scanners, link easily so all staff are in a safe range before each shift.</div>
    <p class="copy" style="left:14px;top:290px;width:276px;text-align:center;font-size:4.8px">The device keeps a full record in the cloud for fast reports.<br>Call 1300 555 018 · hello@vantorahealth.com.au</p>
  </div>
</section>

<!-- Spread 3: features and specification -->
<section class="spread specs" style="top:772px;height:418px">
  <div class="page features">
    <div class="photo" role="img" aria-label="Photo of the terminal on a tripod in an office corridor" style="left:0;top:0;width:304px;height:150px;background:linear-gradient(135deg,#dfe4e8,#aeb9c2)"></div>
    <div class="h" style="position:absolute;left:186px;top:112px;width:110px;font-size:5.5px;color:var(--navy)">At distance 0.5 – 1m<br>± 0.3°C temperature</div>
    <div style="position:absolute;left:14px;top:160px;width:150px;height:118px;background:var(--blue);padding:6px">
      <div class="h" style="font-size:7px;color:#fff;margin-bottom:3px">Key features</div>
      <ul class="list">
        <li>Measures body heat in 0.5 seconds</li>
        <li>Contact-free check at the entrance</li>
        <li>Face recognition with mask alert</li>
        <li>Cloud reports from any device</li>
        <li>Links to doors and payroll systems</li>
        <li>Voice prompts and live alarm</li>
        <li>Blacklist set in the cloud app</li>
        <li>Stores up to 30,000 face records</li>
      </ul>
    </div>
    <div class="photo" role="img" aria-label="Photo of the terminal on a floor stand" style="left:176px;top:160px;width:114px;height:240px;background:linear-gradient(180deg,#e8ecef,#b7c2ca)"></div>
    <div style="position:absolute;left:14px;top:284px;width:150px;height:118px;background:var(--teal);padding:6px">
      <div class="h" style="font-size:7px;color:#fff;margin-bottom:3px">Advantages</div>
      <ul class="list">
        <li>Quick and easy install</li>
        <li>No queue at the front door</li>
        <li>Accurate to ± 0.3°C</li>
        <li>Works with existing access control</li>
        <li>Daily reports sent by email</li>
        <li>Safe for staff and visitors</li>
        <li>Local support and service</li>
      </ul>
    </div>
  </div>
  <div class="page spec-page">
    <div class="spec-title h">Product specification</div>
    <table class="spec" style="left:14px;top:36px;width:276px">
      <tr><td class="g" rowspan="5">System</td><td class="k">Screen</td><td>8 inch IPS touch display</td></tr>
      <tr><td class="k">Processor</td><td>Quad core 1.8 GHz</td></tr>
      <tr><td class="k">Memory</td><td>2 GB RAM / 16 GB storage</td></tr>
      <tr><td class="k">Operating system</td><td>Embedded Linux</td></tr>
      <tr><td class="k">Face capacity</td><td>30,000 faces</td></tr>
      <tr><td class="g" rowspan="5">Camera</td><td class="k">Sensor</td><td>2 MP wide dynamic range</td></tr>
      <tr><td class="k">Lens</td><td>Dual lens, 4 mm</td></tr>
      <tr><td class="k">Recognition speed</td><td>Under 0.5 seconds</td></tr>
      <tr><td class="k">Recognition range</td><td>0.5 m to 2 m</td></tr>
      <tr><td class="k">Light</td><td>Infrared fill light</td></tr>
      <tr><td class="g" rowspan="5">Thermal</td><td class="k">Thermal sensor</td><td>Uncooled array, 32 × 32</td></tr>
      <tr><td class="k">Range</td><td>30°C to 45°C</td></tr>
      <tr><td class="k">Accuracy</td><td>± 0.3°C</td></tr>
      <tr><td class="k">Distance</td><td>0.5 m to 1 m</td></tr>
      <tr><td class="k">Alarm</td><td>Voice and screen alert</td></tr>
      <tr><td class="g" rowspan="5">Interface</td><td class="k">Network</td><td>Ethernet, Wi-Fi</td></tr>
      <tr><td class="k">Relay output</td><td>1 channel door relay</td></tr>
      <tr><td class="k">Wiegand</td><td>Input and output</td></tr>
      <tr><td class="k">USB</td><td>1 port</td></tr>
      <tr><td class="k">Cloud</td><td>Live reports and blacklist</td></tr>
      <tr><td class="g" rowspan="5">General</td><td class="k">Power</td><td>DC 12 V / 2 A</td></tr>
      <tr><td class="k">Working temp</td><td>0°C to 50°C</td></tr>
      <tr><td class="k">Humidity</td><td>10% to 90%</td></tr>
      <tr><td class="k">Size</td><td>260 × 130 × 25 mm</td></tr>
      <tr><td class="k">Mounting</td><td>Floor stand, wall or turnstile</td></tr>
      <tr><td class="g" rowspan="4">Support</td><td class="k">Warranty</td><td>2 years</td></tr>
      <tr><td class="k">Updates</td><td>Free cloud updates</td></tr>
      <tr><td class="k">Languages</td><td>English and more</td></tr>
      <tr><td class="k">Service</td><td>Local team support</td></tr>
    </table>
  </div>
</section>

</body>
</html>
```